Book project Beatrix

I'm looking for a book cover idea and layout of the text for the chapter in part 1 and part 2.

I'm a dentist grew up in Sweden living in Chicago since 24 years. I've been working on a book for the past 4 years where I'm trying to convey the idea that your overall wellbeing is dependent on an holistic approach centered on your oral health. It all begins in the mouth!

I talk about my experiences and learnings as a Swedish -American, who has played professional golf, worked as a dentist in Sweden, researching mobile dental care (barriers to health), being a serial entrepreneur, including being the founder of BrightvaleForum, public health advocate, mother of 4, grandmother and wife.

In part 1 of the book I talk about the mouth and the mouth-body connection. Part 2 (the solutions) are 4 pillars, Eat, Sleep, Breathe and Move (your body and mind) for better overall wellbeing. I also hav a chapter about Habits. How to create your habits you want for success. Each pillar chapter ends with a worksheet for the reader to use to create new habits.

My style is more on the minimilist and simple less is more spectrum. I don't like clutter.. Most of my clothes are black - I use material to make outfits different. My home is black white and grey with an accent color of red.

I'm open minded that there are other choices than a black book.
My favorite book look is Petra Lindvoss's book

The title of the book is Lumo - a Nordic-rooted handbook for calm days that begins at your lips

Please play around with concepts of a mouth (think Velvet Harrows perhaps), using the O for mouth etc. I am looking for creative ideas that would make the book be attractive, stand out, create trials etc.

Target Market(s)

The health conscious person

Industry/Entity Type

wellness overall health

Font styles to use
Sans Serif

Colors

Designer to choose colors to be used in the design.

Requirements
Must have
• a book cover idea including titel and subtitel the swedish word MUNHÄLSA on the cover as well.
Nice to have
• book cover that draws the attention to mouth as the gateway
Should not have
• Color see upload file

```html
<!DOCTYPE html>
<html lang="sv">
<head>
<meta charset="utf-8">
<title>Lumo – Munhälsa – Book Cover</title>
<link rel="stylesheet" href="https://fonts.googleapis.com/css2?family=Montserrat:wght@200;300;800&display=swap">
<style>
  :root {
    --backdrop: #e4e4e6;
    --cover-black: #262626;
    --ink-white: #f4f4f4;
    --accent-red: #e8343b;
  }
  * { margin: 0; padding: 0; box-sizing: border-box; }
  html, body {
    width: 1200px;
    height: 1000px;
    overflow: hidden;
    background: var(--backdrop);
  }
  .canvas {
    position: relative;
    width: 1200px;
    height: 1000px;
    display: flex;
    align-items: center;
    justify-content: center;
  }
  .book-cover {
    position: relative;
    width: 600px;
    height: 880px;
    background: var(--cover-black);
    color: var(--ink-white);
    font-family: "Montserrat", sans-serif;
    overflow: hidden;
  }
  .mouth-mark {
    position: absolute;
    left: 0;
    top: 235px;
    width: 118px;
    height: 150px;
  }
  .title-block {
    position: absolute;
    left: 128px;
    top: 222px;
  }
  .book-title {
    font-weight: 800;
    font-size: 122px;
    line-height: 1;
    letter-spacing: 2px;
  }
  .book-subtitle {
    margin-top: 10px;
    font-weight: 200;
    font-size: 58px;
    line-height: 1;
    letter-spacing: 4px;
  }
  .author-name {
    position: absolute;
    right: 44px;
    bottom: 60px;
    font-weight: 300;
    font-size: 30px;
    letter-spacing: 4px;
  }
</style>
</head>
<body>
  <main class="canvas">
    <section class="book-cover">
      <svg class="mouth-mark" viewBox="0 0 118 150" role="img" aria-label="Illustration of open red lips forming the letter O">
        <ellipse cx="50" cy="75" rx="62" ry="72" fill="var(--accent-red)"/>
      </svg>
      <div class="title-block">
        <h1 class="book-title">LUMO</h1>
        <p class="book-subtitle">MUNHÄLSA</p>
      </div>
      <p class="author-name">BEATRIX SURNAME</p>
    </section>
  </main>
</body>
</html>
```